Lotus Bowl take out menu

We need a take out menu design using our menu attached. Info to include would be our address: 5817 Meridel Harrow Pkwy #204, Lafayette, LA 70508. Phone number is 337-614-2953. website is www.lotusbowlvtr.example.

Industry/Entity Type

Asian Restaurant

```html
<!DOCTYPE html>
<html lang="en">
<head>
<meta charset="utf-8">
<title>Lotus Bowl Take Out Menu</title>
<link href="https://fonts.googleapis.com/css2?family=Crimson+Pro:wght@400;600;700&family=Open+Sans:wght@400;600;700&display=swap" rel="stylesheet">
<style>
:root{
  --red:#c8102e;
  --red-dark:#9e0c22;
  --paper:#f1f1f1;
  --ink:#222;
  --white:#fff;
  --bg:#e9e4da;
}
*{box-sizing:border-box;margin:0;padding:0}
html,body{width:1200px;height:1200px;overflow:hidden;background:var(--bg)}
body{font-family:"Crimson Pro",serif;position:relative}
.sheet{position:absolute;left:60px;width:1080px;height:560px;display:flex;box-shadow:0 4px 14px rgba(0,0,0,.18)}
.sheet--outside{top:30px}
.sheet--inside{top:610px}
.panel{width:360px;height:100%;padding:12px 16px;display:flex;flex-direction:column;justify-content:space-between;overflow:hidden;position:relative}
.panel--light{background:var(--paper);color:var(--ink)}
.panel--red{background:linear-gradient(160deg,var(--red) 0%,var(--red-dark) 100%);color:var(--white)}
.item{border-bottom:1px dotted currentColor;padding-bottom:3px}
.panel--light .item{border-bottom-color:#888}
.panel--red .item{border-bottom-color:rgba(255,255,255,.6)}
.item-row{display:flex;justify-content:space-between;align-items:baseline;font-weight:700;font-size:12.5px;line-height:1.1}
.panel--light .item-name,.panel--light .price{color:var(--red)}
.desc{font-size:10px;line-height:1.15;padding-right:18px}
.spice{display:inline-block;width:4px;height:9px;border-radius:50% 50% 50% 50%/70% 70% 30% 30%;background:currentColor;transform:rotate(35deg);margin-left:3px;vertical-align:-1px}
.panel--light .spice{background:var(--red)}
.section-head{display:flex;align-items:center;gap:6px}
.section-head::before,.section-head::after{content:"";flex:1;height:1.5px}
.panel--light .section-head::before,.panel--light .section-head::after{background:var(--red)}
.panel--red .section-head::before,.panel--red .section-head::after{background:var(--white)}
.pill{font-size:15px;letter-spacing:.5px;padding:1px 22px;text-transform:uppercase;border-radius:3px}
.panel--light .pill{background:var(--red);color:var(--white)}
.panel--red .pill{background:var(--white);color:var(--red)}
.sub-head{text-align:center;font-size:12px;letter-spacing:.5px;text-transform:uppercase}
.panel--light .sub-head{color:var(--ink)}
/* cover */
.cover{padding:0;display:block;background:var(--red)}
.cover-photo{position:absolute;top:0;left:0;right:0;height:230px;background:radial-gradient(circle at 55% 45%,#d9622a 0%,#6a8c2a 35%,#3a1d12 70%,#f4f4f4 100%);clip-path:polygon(0 0,100% 0,100% 78%,0 100%)}
.cover-brand{position:absolute;top:170px;left:0;right:0;height:160px;background:var(--white);clip-path:polygon(0 30%,100% 0,100% 70%,0 100%);display:flex;flex-direction:column;align-items:center;justify-content:center;padding-top:10px}
.brand-name{font-family:"Open Sans",sans-serif;font-weight:700;font-size:30px;color:#111;display:flex;align-items:center;gap:8px}
.brand-dot{width:16px;height:16px;border-radius:50%;background:var(--red)}
.brand-tag{font-family:"Open Sans",sans-serif;font-size:8px;letter-spacing:2px;color:#111;font-weight:600;margin-top:2px}
.cover-body{position:absolute;top:335px;left:0;right:0;text-align:center;color:var(--white);font-family:"Open Sans",sans-serif}
.cover-title{font-family:"Crimson Pro",serif;font-size:42px;letter-spacing:1px;line-height:1}
.icon{display:block;margin:10px auto 4px}
.phone{font-size:22px;font-weight:700}
.address{font-size:12px;font-weight:600;line-height:1.4}
.web{display:flex;align-items:center;margin:14px 18px 0;gap:0}
.web::before,.web::after{content:"";flex:1;height:1.5px;background:var(--white)}
.web span{background:var(--white);color:var(--red);font-size:10.5px;font-weight:600;padding:2px 14px;border-radius:3px}
</style>
</head>
<body>

<section class="sheet sheet--outside">
  <div class="panel panel--light">
    <div class="item"><div class="item-row"><span class="item-name">Sweet &amp; Sour Chicken</span><span class="price">$13</span></div><p class="desc">Crispy Chicken glazed in a homemade sweet &amp; sour marinade</p></div>
    <div class="section-head"><span class="pill">Seafood</span></div>
    <div class="item"><div class="item-row"><span class="item-name">Kung Pao Shrimp<i class="spice"></i></span><span class="price">$16</span></div><p class="desc">Sautéed shrimp with roasted peanuts and scallions, dry red chili and whole Sichuan peppercorns in Kung Pao sauce</p></div>
    <div class="item"><div class="item-row"><span class="item-name">Rice Wine Shrimp &amp; Tofu<i class="spice"></i></span><span class="price">$18</span></div><p class="desc">Shrimp and Tofu braised in garlic pickled pepper sauce with rice wine</p></div>
    <div class="item"><div class="item-row"><span class="item-name">Shrimp in Spicy Garlic Sauce<i class="spice"></i></span><span class="price">$15</span></div><p class="desc">Shrimp sautéed with jicama ginger, garlic and scallions in a spicy garlic sauce</p></div>
    <div class="item"><div class="item-row"><span class="item-name">Lemon Peel Shrimp</span><span class="price">$15</span></div><p class="desc">Shrimp with fresh lemons in a sweet lemon sauce with vegetables</p></div>
    <div class="item"><div class="item-row"><span class="item-name">Rice Wine Fish<i class="spice"></i></span><span class="price">$14</span></div><p class="desc">White fish filet braised in pickled pepper sauce with rice wine</p></div>
    <div class="section-head"><span class="pill">Noodles &amp; Rice</span></div>
    <div class="item"><div class="item-row"><span class="item-name">Lotus Bowl Fried Rice</span><span class="price">$12</span></div><p class="desc">Shrimp, chicken, and beef, farm fresh eggs, onions, and scallions</p></div>
    <div class="item"><div class="item-row"><span class="item-name">Vegetarian White Fried Rice</span><span class="price">$10</span></div><p class="desc">Mixed vegetables with white rice</p></div>
    <div class="item"><div class="item-row"><span class="item-name">Lotus Bowl Lo Mein</span><span class="price">$12</span></div><p class="desc">Shrimp, chicken, and beef, farm fresh eggs, onions, and scallions</p></div>
    <div class="item"><div class="item-row"><span class="item-name">Vegetarian Lo Mein</span><span class="price">$10</span></div><p class="desc">Mixed vegetables with lo mein noodles</p></div>
    <div class="section-head"><span class="pill">Vegetarian Dishes</span></div>
    <div class="item"><div class="item-row"><span class="item-name">Wok Tossed String Beans<i class="spice"></i></span><span class="price">$9</span></div><p class="desc">Fresh string beans mixed with pickled vegetables</p></div>
  </div>

  <div class="panel panel--red">
    <div class="item"><div class="item-row"><span>Mapo Tofu<i class="spice"></i><i class="spice"></i></span><span>$11</span></div><p class="desc">Soft Tofu, scallion, Sichuan peppercorn and peppers</p></div>
    <div class="item"><div class="item-row"><span>Spicy Garlic Eggplant<i class="spice"></i></span><span>$12</span></div><p class="desc">Chinese eggplant in spicy garlic sauce drizzled with scallions</p></div>
    <div class="item"><div class="item-row"><span>Buddha's Delight</span><span>$10</span></div><p class="desc">Seasonal vegetables wok-tossed in our light soy garlic sauce</p></div>
    <div class="item"><div class="item-row"><span>Stir-fried Eggplant Beans<i class="spice"></i></span><span>$12</span></div><p class="desc">Chinese eggplant with sautéed green beans</p></div>
    <div class="item"><div class="item-row"><span>Shiitake Baby Bok-Choy</span><span>$12</span></div><p class="desc">Sautéed baby bok-choy with Shiitake mushrooms in brown sauce</p></div>
    <div class="section-head"><span class="pill">Kids Menu</span></div>
    <div class="item"><div class="item-row"><span>Beef Lo Mein</span><span>$5</span></div><p class="desc">Lo Mein noodles mixed with beef in garlic sauce</p></div>
    <div class="item"><div class="item-row"><span>Chicken Fried Rice</span><span>$5</span></div><p class="desc">Fried rice, farm fresh eggs, onions, and scallions</p></div>
    <div class="item"><div class="item-row"><span>Sweet &amp; Sour Chicken</span><span>$6</span></div><p class="desc">Bite sized crispy chicken with sweet &amp; sour sauce</p></div>
    <div class="item"><div class="item-row"><span>Lemon Chicken</span><span>$6</span></div><p class="desc">Bite sized crispy chicken in a sweet lemon sauce</p></div>
    <div class="section-head"><span class="pill">Desserts</span></div>
    <div class="item"><div class="item-row"><span>The Great Wall of Cake</span><span>$7</span></div><p class="desc">Scale this fortress of Chocolate Cake Delight</p></div>
    <div class="item"><div class="item-row"><span>Cheesecake Wontons (4)</span><span>$6</span></div><p class="desc">Fried wontons stuffed with cheesecake and dipped in raspberry sauce</p></div>
    <div class="item"><div class="item-row"><span>Tempura Snowball</span><span>$4</span></div><p class="desc">Vanilla ice cream fried in tempura batter with powdered sugar and fudge</p></div>
    <div class="item"><div class="item-row"><span>Sweet Rice Patties in Caramel</span><span>$7</span></div><p class="desc">Traditional Chinese dessert with sweet rice dipped in a caramel sauce</p></div>
  </div>

  <div class="panel panel--red cover">
    <div class="cover-photo" role="img" aria-label="Photo of a stir-fried dish with peppers and glazed meat on a white plate"></div>
    <div class="cover-brand">
      <div class="brand-name"><span class="brand-dot"></span>Lotus Bowl</div>
      <div class="brand-tag">FRESH ASIAN CUISINE</div>
    </div>
    <div class="cover-body">
      <h1 class="cover-title">MENU</h1>
      <svg class="icon" width="28" height="28" viewBox="0 0 28 28" aria-hidden="true"><circle cx="14" cy="14" r="12.5" fill="none" stroke="#fff" stroke-width="1.5"/><path d="M10 8c1 0 1.6 2.4 1.6 3 0 .8-1 1-1 1.6 0 1 2.4 3.8 3.6 3.8.6 0 .8-1 1.6-1 .6 0 3 .6 3 1.6 0 1.2-1.4 2.2-2.6 2.2-3.4 0-8.4-5-8.4-8.4C7.8 9.4 8.8 8 10 8z" fill="#fff"/></svg>
      <div class="phone">337-614-2953</div>
      <svg class="icon" width="28" height="28" viewBox="0 0 28 28" aria-hidden="true"><circle cx="14" cy="14" r="12.5" fill="none" stroke="#fff" stroke-width="1.5"/><path d="M14 6.5a5 5 0 0 0-5 5c0 3.8 5 9.5 5 9.5s5-5.7 5-9.5a5 5 0 0 0-5-5zm0 7a2 2 0 1 1 0-4 2 2 0 0 1 0 4z" fill="#fff"/></svg>
      <p class="address">5817 Meridel Harrow Pkwy,<br>#204, Lafayette, LA 70508</p>
      <div class="web"><span>www.lotusbowlvtr.example</span></div>
    </div>
  </div>
</section>

<section class="sheet sheet--inside">
  <div class="panel panel--red">
    <div class="section-head"><span class="pill">Appetizers</span></div>
    <div class="item"><div class="item-row"><span>Edamame</span><span>$4</span></div><p class="desc">Seasoned &amp; boiled soy bean</p></div>
    <div class="item"><div class="item-row"><span>Scallion Pancakes</span><span>$6</span></div><p class="desc">Traditional Chinese flatbread folded with oil and minced scallions and pan fried</p></div>
    <div class="item"><div class="item-row"><span>Lotus Bowl Lettuce Wraps</span><span>$8</span></div><p class="desc">Seasoned ground chicken drizzled with our top secret homemade sauce served with lettuce wraps</p></div>
    <div class="item"><div class="item-row"><span>Salt &amp; Pepper Calamari</span><span>$9</span></div><p class="desc">Crispy Calamari with green &amp; red peppers and onions</p></div>
    <div class="item"><div class="item-row"><span>Buddha Bang Shrimp</span><span>$9</span></div><p class="desc">Crispy fried shrimp tossed in our creamy spicy sauce</p></div>
    <div class="item"><div class="item-row"><span>Drunken Chicken<i class="spice"></i></span><span>$8</span></div><p class="desc">Chicken, Thai chili in a house made spicy sauce</p></div>
    <div class="item"><div class="item-row"><span>Sichuan Spiced Beef<i class="spice"></i><i class="spice"></i></span><span>$9</span></div><p class="desc">Beef Shank, beef tripe, cilantro, peanuts and celery</p></div>
    <div class="item"><div class="item-row"><span>Beef Crispy Bottom Bao</span><span>$10</span></div><p class="desc">Pan fried crispy bottom Bao, stuffed with beef and shrimp, drizzled with scallion and sesame (Fresh made to order, takes at least 20 mins to serve)</p></div>
    <div class="item"><div class="item-row"><span>Shrimp &amp; Beef Crispy Bottom Bao</span><span>$10</span></div><p class="desc">Pan fried crispy bottom Bao, stuffed with beef, drizzle with scallion and sesame (Fresh made to order, takes at least 20 mins to serve)</p></div>
    <div class="item"><div class="item-row"><span>Crispy Mala Beef Jerky<i class="spice"></i><i class="spice"></i></span><span>$9</span></div><p class="desc">Dry fried shredded beef with various peppers in sesame and peppercorn oil</p></div>
    <div class="item"><div class="item-row"><span>Fried Chicken Dumplings (6)</span><span>$6</span></div><p class="desc">Chinese dumpling stuffed with Chicken, Shiitake mushrooms and bamboo shoots</p></div>
    <div class="item"><div class="item-row"><span>Red Oil Dumplings (6)<i class="spice"></i></span><span>$7</span></div><p class="desc">Pork filled dumplings in Sichuan red oil sauce drizzled with sesame</p></div>
  </div>

  <div class="panel panel--red">
    <div class="item"><div class="item-row"><span>Pork Egg Rolls (2)</span><span>$4</span></div><p class="desc">Hand rolled with julienned veggies with our sweet n' sour mustard sauce</p></div>
    <div class="item"><div class="item-row"><span>Vegetarian Spring Rolls (3)</span><span>$4</span></div><p class="desc">Traditional Asian Roll served with a sweet chili sauce</p></div>
    <div class="item"><div class="item-row"><span>Garlic Cucumber Salad</span><span>$7</span></div><p class="desc">Sliced cucumber with a garlic vinaigrette</p></div>
    <div class="item"><div class="item-row"><span>Hot n' Sour Soup<i class="spice"></i></span><span>$4</span></div><p class="desc">Tangy broth with Bamboo shoot, wood ear fungus, tofu, egg and carrots</p></div>
    <div class="item"><div class="item-row"><span>West Lake Soup</span><span>$4</span></div><p class="desc">Light creamy soup with ground beef, diced Shiitake mushroom, tofu, bamboo shoots, egg white and cilantro</p></div>
    <div class="section-head"><span class="pill">Entrees</span></div>
    <div class="sub-head">Chef Specialties</div>
    <div class="item"><div class="item-row"><span>Jasmine Tea Smoked Duck</span><span>$24</span></div><p class="desc">Boneless half duck served with thinly sliced cucumber, scallion, house made duck sauce and soft flour wrap</p></div>
    <div class="item"><div class="item-row"><span>Sizzling Cumin' Lamb<i class="spice"></i></span><span>$16</span></div><p class="desc">Tender pieces of lamb rubbed in cumin, Sichuan peppers, celery and cilantro</p></div>
    <div class="item"><div class="item-row"><span>Chef Lin's Spicy Beef<i class="spice"></i><i class="spice"></i></span><span>$16</span></div><p class="desc">Angus beef in house made green peppercorn sauce, drizzled with fresh Sichuan peppercorn, Thai chili and cilantro</p></div>
    <div class="item"><div class="item-row"><span>Chef Lin's Spicy Fish<i class="spice"></i><i class="spice"></i></span><span>$17</span></div><p class="desc">Fish filet in house made green peppercorn sauce, drizzled with fresh Sichuan peppercorn, Thai chili and cilantro</p></div>
    <div class="item"><div class="item-row"><span>General Tso's Scallops<i class="spice"></i></span><span>$18</span></div><p class="desc">The perfect combination of tender scallops marinated in a sweet chili sauce with broccoli and red peppers</p></div>
    <div class="sub-head">Beef &amp; Pork</div>
    <div class="item"><div class="item-row"><span>Dancing Beef<i class="spice"></i><i class="spice"></i><i class="spice"></i></span><span>$16</span></div><p class="desc">Angus Beef slices on a bed of sizzling rice crackers, black peppercorn and Thai chili</p></div>
  </div>

  <div class="panel panel--light">
    <div class="item"><div class="item-row"><span class="item-name">Oyster Beef</span><span class="price">$14</span></div><p class="desc">Tender cuts of steak wok fried and marinated in a homemade oyster sauce</p></div>
    <div class="item"><div class="item-row"><span class="item-name">Double Pepper Beef<i class="spice"></i><i class="spice"></i><i class="spice"></i></span><span class="price">$16</span></div><p class="desc">Angus Steak cubes with fresh green peppercorn, Thai chili, Serrano Pepper and celery</p></div>
    <div class="item"><div class="item-row"><span class="item-name">Black Pepper Steak<i class="spice"></i></span><span class="price">$15</span></div><p class="desc">Tender cuts of steak mixed with onions and red and green bell peppers</p></div>
    <div class="item"><div class="item-row"><span class="item-name">Singapore Baby Back Ribs</span><span class="price">$16</span></div><p class="desc">Tender Baby back ribs rubbed in a Thai inspired sweet tangy glaze</p></div>
    <div class="item"><div class="item-row"><span class="item-name">Dancing Pork Belly</span><span class="price">$15</span></div><p class="desc">Braised Pork Belly on sizzling rice cracker</p></div>
    <div class="item"><div class="item-row"><span class="item-name">Twice Cooked Pork<i class="spice"></i></span><span class="price">$14</span></div><p class="desc">Stir fried Pork Belly slices with leek and fermented black beans</p></div>
    <div class="sub-head">Chicken</div>
    <div class="item"><div class="item-row"><span class="item-name">Kung Pao Chicken<i class="spice"></i></span><span class="price">$13</span></div><p class="desc">Chicken sautéed with roasted peanuts and scallions, dry red chili and whole Sichuan peppercorns in Kung Pao sauce</p></div>
    <div class="item"><div class="item-row"><span class="item-name">Orange Chicken</span><span class="price">$13</span></div><p class="desc">Battered-fried chicken breast with dried chili peppers and stir fried in a tangy orange flavored sauce</p></div>
    <div class="item"><div class="item-row"><span class="item-name">Double Pepper Chicken<i class="spice"></i><i class="spice"></i><i class="spice"></i></span><span class="price">$15</span></div><p class="desc">Farm raised chicken cube with fresh green peppercorn, Thai chili, Serrano peppers, and jalapenos</p></div>
    <div class="item"><div class="item-row"><span class="item-name">Crispy Spicy Chicken<i class="spice"></i><i class="spice"></i></span><span class="price">$14</span></div><p class="desc">Crispy diced chicken with Sichuan peppers, cilantro and sesame</p></div>
    <div class="item"><div class="item-row"><span class="item-name">General Tso's Chicken<i class="spice"></i></span><span class="price">$13</span></div><p class="desc">Battered-fried chicken breast, stir-fried in a sweet &amp; tangy chili sauce, scallions and chili pepper</p></div>
    <div class="item"><div class="item-row"><span class="item-name">Shredded Chicken in Spicy Garlic Sauce<i class="spice"></i></span><span class="price">$14</span></div><p class="desc">Tender shredded chicken, wood ear fungus, bamboo shoots in a classic spicy garlic sauce</p></div>
  </div>
</section>

</body>
</html>
```